Help create our baby! Modern facial bar website.

We want a RESPONSIVE Wordpress website that is clean, gender neutral, and modern. Mobile first is the way to go. This must look awesome on a mobile device. We are opening a modern and fresh organic mask bar with modern decor. Think clean, fresh, airy. We will also offer other services. We will offer many of the services that movie stars have access to, such as Light Therapy, Oxygen Facial, Microcurrent, Microderm, etc. Think express facial bar that is results driven. Our niche is for busy men and women who want to see results, and don't have a lot of time to spend at a spa. We are not a traditional spa. So no walking around in robes. Our services are half the cost when compared to traditional spas.

We will offer a membership program with different tiers of memberships. This is something that we want to franchise if our location is successful.

We are not into a typical spa/massage website type design with lots of commonly used images of people getting massages and facials.

We are thinking of a white background, with pops of color that are the same as our logo.

Please include the following hex codes in the website (don't think these are exact...we'd like to match the provided logo):
ea8e05
9ca0a8
14c5d4

The font of our logo is Coolvetica RG.

Target Market(s)

Young, hip, busy professionals who want to take care of their skin. Men, women, teens. Metropolitan US city.

Industry/Entity Type

Skin Care Product

Coding

Coded - Design and coding required

Font styles to use
Sans Serif

Requirements
Must have
• Modern, clean, fresh website. White background with pops of color. We need to be able to edit the text and add services through Wordpress.
Nice to have
• Pictures of men and women having fun. Some could have creams and products on their face. We want to promote facial parties. SEO is very important to us, so please design with that in mind.
Should not have
• No clip art. No cheesy pictures of women getting massages and facials. We want to avoid looking like one of the many places that do "facials" but do not really specialize in skincare. We want to avoid looking like a Nail place, or foot spa place that also does facials (so...no butterflies, leaves, and flowers).

```html
<!DOCTYPE html>
<html lang="en">
<head>
<meta charset="utf-8">
<title>Lumabar — Modern Facial Bar</title>
<link rel="stylesheet" href="https://fonts.googleapis.com/css2?family=Open+Sans:wght@400;600;700&family=Raleway:wght@500;600;700;800&display=swap">
<style>
:root{
  --orange:#ea8e05;
  --teal:#14c5d4;
  --grey:#9ca0a8;
  --ink:#222;
  --text:#666;
  --light:#f4f4f4;
  --footer:#1e1e1e;
  --white:#fff;
}
*{box-sizing:border-box;margin:0;padding:0}
html,body{width:1200px;height:2375px;overflow:hidden;background:var(--white)}
body{position:relative;font-family:"Open Sans",Arial,sans-serif;color:var(--text)}
a{color:inherit;text-decoration:none}
.abs{position:absolute}

/* header */
.site-header{position:absolute;left:0;top:0;width:1200px;height:80px;border-top:3px solid var(--orange);background:var(--white)}
.brand{position:absolute;left:98px;top:16px;font-family:"Raleway",sans-serif;font-weight:700;font-size:40px;letter-spacing:-1px;color:var(--teal);line-height:44px}
.main-nav{position:absolute;left:358px;top:28px;display:flex;gap:0;font-family:"Raleway",sans-serif;font-weight:600;font-size:15px;color:var(--ink)}
.main-nav a{margin-right:26px}
.main-nav a.active{color:var(--orange)}
.search-icon{position:absolute;left:836px;top:31px}
.call-btn{position:absolute;left:876px;top:22px;width:224px;height:36px;background:var(--teal);color:var(--white);font-family:"Raleway",sans-serif;font-weight:700;font-size:12.5px;display:flex;align-items:center;justify-content:center;letter-spacing:.2px}

/* hero */
.hero{position:absolute;left:0;top:80px;width:1200px;height:475px;background:linear-gradient(100deg,#c9873f 0%,#e5833a 30%,#c55a2a 55%,#3b47a8 78%,#6a5fd2 100%)}
.hero-title{position:absolute;left:0;width:1200px;top:145px;text-align:center;font-family:"Raleway",sans-serif;font-weight:800;font-size:66px;color:var(--white);letter-spacing:-1.5px}
.hero-sub{position:absolute;left:0;width:1200px;top:226px;text-align:center;font-size:21px;color:var(--white)}
.book-btn{position:absolute;left:525px;top:276px;width:150px;height:45px;background:var(--orange);color:var(--white);font-family:"Raleway",sans-serif;font-weight:700;font-size:16px;display:flex;align-items:center;justify-content:center}
.arrow{position:absolute}

/* about */
.about-photo{position:absolute;left:98px;top:605px;width:374px;height:312px;background:linear-gradient(135deg,#b9c0e6,#a99a8c 60%,#8d7561)}
.about{position:absolute;left:517px;top:600px;width:583px}
.section-title{font-family:"Raleway",sans-serif;font-weight:800;font-size:20px;color:var(--ink);letter-spacing:-.3px}
.about p{font-size:12px;line-height:22px;margin-top:18px}
.about .section-title{margin-bottom:8px}
.read-more{font-family:"Open Sans",sans-serif;font-weight:700;font-size:12.5px;color:var(--orange)}
.about .read-more{display:block;margin-top:18px}

/* services */
.services{position:absolute;left:0;top:967px;width:1200px;height:474px;background:var(--teal)}
.services .section-title{position:absolute;left:0;width:1200px;top:47px;text-align:center;color:var(--white)}
.service{position:absolute;top:95px;width:240px;text-align:center;color:var(--white)}
.service-photo{width:210px;height:210px;margin:0 auto;border-radius:50%;border:6px solid #8fe6ee}
.service h3{font-family:"Raleway",sans-serif;font-weight:600;font-size:19px;margin-top:14px}
.service p{font-size:13px;line-height:20px;margin-top:8px}
.service .read-more{display:block;color:var(--white);margin-top:12px}

/* plans */
.plans-title{position:absolute;left:0;top:1486px;width:1200px;text-align:center}
.plans-intro{position:absolute;left:180px;top:1535px;width:840px;text-align:center;font-size:12px;line-height:22px}
.plan{position:absolute;top:1612px;width:317px;height:410px;border:1px solid #ddd;border-radius:6px;background:var(--white);box-shadow:0 2px 6px rgba(0,0,0,.08);overflow:hidden}
.plan-head{height:46px;color:var(--white);font-family:"Raleway",sans-serif;font-weight:800;font-size:17px;display:flex;align-items:center;justify-content:center}
.plan-price{height:70px;background:var(--light);display:flex;align-items:center;justify-content:center;color:#333;font-family:"Open Sans",sans-serif}
.plan-price .amount{font-weight:700;font-size:38px;letter-spacing:-1px}
.plan-price sup{font-size:18px;font-weight:700;vertical-align:14px}
.plan-price .per{font-size:14px;font-weight:600;margin-left:8px;margin-top:14px}
.plan ul{list-style:none;margin-top:22px;text-align:center}
.plan li{font-size:13px;height:36px;line-height:36px}
.plan li b{color:#222;font-weight:600}
.plan li svg{vertical-align:-1px;margin-right:6px}
.signup{position:absolute;left:50%;transform:translateX(-50%);top:341px;width:138px;height:37px;color:var(--white);font-family:"Open Sans",sans-serif;font-weight:700;font-size:15px;display:flex;align-items:center;justify-content:center}
.t-orange{background:var(--orange)}
.t-teal{background:var(--teal)}
.t-grey{background:var(--grey)}

/* footer */
.site-footer{position:absolute;left:0;top:2078px;width:1200px;height:297px;background:var(--footer);border-top:3px solid var(--teal);color:#ddd}
.footer-brand{position:absolute;left:98px;top:60px;font-family:"Raleway",sans-serif;font-weight:700;font-size:56px;color:var(--white);letter-spacing:-1.5px}
.footer-col{position:absolute;top:44px}
.footer-col h4{font-family:"Raleway",sans-serif;font-weight:800;font-size:16px;color:var(--white);margin-bottom:18px}
.footer-links a{display:block;font-size:12px;line-height:22px}
.footer-col p{font-size:12px;line-height:20px}
.email-field{width:263px;height:32px;background:var(--white);margin-top:12px;color:#777;font-size:12px;padding-left:9px;line-height:32px}
.subscribe{display:inline-block;margin-top:12px;border:2px solid var(--white);border-radius:3px;padding:4px 10px;font-weight:700;font-size:12px;color:var(--white)}
.contact-row{display:flex;gap:18px;font-size:12px;line-height:19px;margin-bottom:18px}
.contact-row svg{flex:none;margin-top:2px}
.footer-rule{position:absolute;left:98px;top:230px;width:1004px;height:1px;background:#333}
.copyright{position:absolute;left:98px;top:257px;font-size:12px}
.social{position:absolute;left:948px;top:246px;display:flex;gap:8px}
.social span{width:32px;height:32px;border:2px solid var(--white);border-radius:50%}
</style>
</head>
<body>

<header class="site-header">
  <div class="brand">lumabar</div>
  <nav class="main-nav">
    <a class="active" href="#">Home</a>
    <a href="#">About Us</a>
    <a href="#">Services</a>
    <a href="#">Products</a>
    <a href="#">Plans</a>
    <a href="#">Contact Us</a>
  </nav>
  <svg class="search-icon" width="16" height="16" viewBox="0 0 16 16"><circle cx="6.5" cy="6.5" r="5" fill="none" stroke="#222" stroke-width="2"/><line x1="10.2" y1="10.2" x2="14.5" y2="14.5" stroke="#222" stroke-width="2.4" stroke-linecap="round"/></svg>
  <a class="call-btn" href="#">CLICK TO CALL PHONE NUMBER</a>
</header>

<section class="hero" role="img" aria-label="Woman relaxing during a light therapy facial in a colourful modern bar">
  <svg class="arrow" style="left:54px;top:222px" width="18" height="32" viewBox="0 0 18 32"><polyline points="15,2 3,16 15,30" fill="none" stroke="rgba(255,255,255,.7)" stroke-width="3"/></svg>
  <svg class="arrow" style="left:1128px;top:222px" width="18" height="32" viewBox="0 0 18 32"><polyline points="3,2 15,16 3,30" fill="none" stroke="rgba(255,255,255,.7)" stroke-width="3"/></svg>
  <h1 class="hero-title">Lumabar</h1>
  <p class="hero-sub">We are opening a modern and fresh organic mask bar with modern decor.</p>
  <a class="book-btn" href="#">BOOK NOW</a>
</section>

<div class="about-photo" role="img" aria-label="Laughing man wearing a grey clay face mask"></div>
<section class="about">
  <h2 class="section-title">ABOUT US</h2>
  <p>Lumabar was born after it's founder Dana Whitley, a busy mom of 3 decided after her last facial that she is tired of wasting hours of her day and paying exorbitant prices to have products smeared on her face with no real visible results.</p>
  <p>"I remember lying on the table having my Esthetician trying to sell me everything under the sun while smearing products on my skin (which looked great when I walked out but absolutely no difference in my skin even after regular once a month facials." quoted Dana Whitley. So for us we believe the tradition of lying in a dark room for hours is a thing of the past. We created an open facial bar offering treatments that achieve incredible outcomes. We are not like other facial spas. We offer fresh hand made products on our spa bar along with medical style services.</p>
  <a class="read-more" href="#">READ MORE &gt;&gt;</a>
</section>

<section class="services">
  <h2 class="section-title">OUR SERVICES</h2>
  <svg class="arrow" style="left:64px;top:190px" width="12" height="22" viewBox="0 0 12 22"><polyline points="10,2 2,11 10,20" fill="none" stroke="rgba(255,255,255,.8)" stroke-width="2.5"/></svg>
  <svg class="arrow" style="left:1122px;top:190px" width="12" height="22" viewBox="0 0 12 22"><polyline points="2,2 10,11 2,20" fill="none" stroke="rgba(255,255,255,.8)" stroke-width="2.5"/></svg>

  <article class="service" style="left:87px">
    <div class="service-photo" role="img" aria-label="Client receiving a light therapy treatment" style="background:linear-gradient(135deg,#d9c7e8,#b59ad2 55%,#8f74b5)"></div>
    <h3>Light Therapy</h3>
    <p>At vero eos et accusamus et iusto odio dignissimos ducimus qui blanditiis praesentium voluptatum del</p>
    <a class="read-more" href="#">READ MORE &gt;&gt;</a>
  </article>
  <article class="service" style="left:349px">
    <div class="service-photo" role="img" aria-label="Young client during an oxygen facial" style="background:linear-gradient(135deg,#3f7fb8,#6d88a8 50%,#d2a98a)"></div>
    <h3>Oxygen Facial</h3>
    <p>At vero eos et accusamus et iusto odio dignissimos ducimus qui blanditiis praesentium voluptatum del</p>
    <a class="read-more" href="#">READ MORE &gt;&gt;</a>
  </article>
  <article class="service" style="left:610px">
    <div class="service-photo" role="img" aria-label="Client receiving a microcurrent facial treatment" style="background:linear-gradient(135deg,#8fc3e0,#e4c6b4 55%,#b8d6e6)"></div>
    <h3>Microcurrent</h3>
    <p>At vero eos et accusamus et iusto odio dignissimos ducimus qui blanditiis praesentium voluptatum del</p>
    <a class="read-more" href="#">READ MORE &gt;&gt;</a>
  </article>
  <article class="service" style="left:872px">
    <div class="service-photo" role="img" aria-label="Client receiving a microdermabrasion treatment" style="background:linear-gradient(135deg,#eee4dc,#e0bca8 55%,#5a3b2e)"></div>
    <h3>Microderm</h3>
    <p>At vero eos et accusamus et iusto odio dignissimos ducimus qui blanditiis praesentium voluptatum del</p>
    <a class="read-more" href="#">READ MORE &gt;&gt;</a>
  </article>
</section>

<h2 class="section-title plans-title">PLANS</h2>
<p class="plans-intro">At vero eos et accusamus et iusto odio dignissimos ducimus qui blanditiis praesentium voluptatum deleniti atque corrupti quos dolores et quas molestias excepturi sint occaecati cupiditate non provident, similique sunt in culpa qui officia deserunt mollitia animi, id e</p>

<article class="plan" style="left:98px">
  <div class="plan-head t-orange">MEMBERSHIP 1</div>
  <div class="plan-price"><span class="amount">$44<sup>99</sup></span><span class="per">Per month</span></div>
  <ul>
    <li><svg width="12" height="10" viewBox="0 0 12 10"><polyline points="1,5 4.5,8.5 11,1.5" fill="none" stroke="#ea8e05" stroke-width="2.2"/></svg>At vero eos et accusamus et &nbsp;: <b>$56</b></li>
    <li><svg width="12" height="10" viewBox="0 0 12 10"><polyline points="1,5 4.5,8.5 11,1.5" fill="none" stroke="#ea8e05" stroke-width="2.2"/></svg>Blanditiis praesent &nbsp;: &nbsp;<b>$60</b></li>
    <li><svg width="12" height="10" viewBox="0 0 12 10"><polyline points="1,5 4.5,8.5 11,1.5" fill="none" stroke="#ea8e05" stroke-width="2.2"/></svg>Dignissimos duci qui &nbsp;: &nbsp;<b>$600 &nbsp;Monthly</b></li>
    <li><svg width="12" height="10" viewBox="0 0 12 10"><polyline points="1,5 4.5,8.5 11,1.5" fill="none" stroke="#ea8e05" stroke-width="2.2"/></svg>Sit voluptatem accusa &nbsp;: &nbsp;<b>$4</b></li>
    <li><svg width="12" height="10" viewBox="0 0 12 10"><polyline points="1,5 4.5,8.5 11,1.5" fill="none" stroke="#ea8e05" stroke-width="2.2"/></svg>Aliquam quaerat &nbsp;: &nbsp;<b>Every 24 hours</b></li>
  </ul>
  <a class="signup t-orange" href="#">SIGN UP NOW!</a>
</article>

<article class="plan" style="left:441px">
  <div class="plan-head t-teal">MEMBERSHIP 2</div>
  <div class="plan-price"><span class="amount">$44<sup>99</sup></span><span class="per">Per month</span></div>
  <ul>
    <li><svg width="12" height="10" viewBox="0 0 12 10"><polyline points="1,5 4.5,8.5 11,1.5" fill="none" stroke="#14c5d4" stroke-width="2.2"/></svg>At vero eos et accusamus et &nbsp;: <b>$56</b></li>
    <li><svg width="12" height="10" viewBox="0 0 12 10"><polyline points="1,5 4.5,8.5 11,1.5" fill="none" stroke="#14c5d4" stroke-width="2.2"/></svg>Blanditiis praesent &nbsp;: &nbsp;<b>$60</b></li>
    <li><svg width="12" height="10" viewBox="0 0 12 10"><polyline points="1,5 4.5,8.5 11,1.5" fill="none" stroke="#14c5d4" stroke-width="2.2"/></svg>Dignissimos duci qui &nbsp;: &nbsp;<b>$600 &nbsp;Monthly</b></li>
    <li><svg width="12" height="10" viewBox="0 0 12 10"><polyline points="1,5 4.5,8.5 11,1.5" fill="none" stroke="#14c5d4" stroke-width="2.2"/></svg>Sit voluptatem accusa &nbsp;: &nbsp;<b>$4</b></li>
    <li><svg width="12" height="10" viewBox="0 0 12 10"><polyline points="1,5 4.5,8.5 11,1.5" fill="none" stroke="#14c5d4" stroke-width="2.2"/></svg>Aliquam quaerat &nbsp;: &nbsp;<b>Every 24 hours</b></li>
  </ul>
  <a class="signup t-teal" href="#">SIGN UP NOW!</a>
</article>

<article class="plan" style="left:784px">
  <div class="plan-head t-grey">MEMBERSHIP 3</div>
  <div class="plan-price"><span class="amount">$44<sup>99</sup></span><span class="per">Per month</span></div>
  <ul>
    <li><svg width="12" height="10" viewBox="0 0 12 10"><polyline points="1,5 4.5,8.5 11,1.5" fill="none" stroke="#9ca0a8" stroke-width="2.2"/></svg>At vero eos et accusamus et &nbsp;: <b>$56</b></li>
    <li><svg width="12" height="10" viewBox="0 0 12 10"><polyline points="1,5 4.5,8.5 11,1.5" fill="none" stroke="#9ca0a8" stroke-width="2.2"/></svg>Blanditiis praesent &nbsp;: &nbsp;<b>$60</b></li>
    <li><svg width="12" height="10" viewBox="0 0 12 10"><polyline points="1,5 4.5,8.5 11,1.5" fill="none" stroke="#9ca0a8" stroke-width="2.2"/></svg>Dignissimos duci qui &nbsp;: &nbsp;<b>$600 &nbsp;Monthly</b></li>
    <li><svg width="12" height="10" viewBox="0 0 12 10"><polyline points="1,5 4.5,8.5 11,1.5" fill="none" stroke="#9ca0a8" stroke-width="2.2"/></svg>Sit voluptatem accusa &nbsp;: &nbsp;<b>$4</b></li>
    <li><svg width="12" height="10" viewBox="0 0 12 10"><polyline points="1,5 4.5,8.5 11,1.5" fill="none" stroke="#9ca0a8" stroke-width="2.2"/></svg>Aliquam quaerat &nbsp;: &nbsp;<b>Every 24 hours</b></li>
  </ul>
  <a class="signup t-grey" href="#">SIGN UP NOW!</a>
</article>

<footer class="site-footer">
  <div class="footer-brand">lumabar</div>

  <div class="footer-col" style="left:422px">
    <h4>INFORMATION</h4>
    <nav class="footer-links">
      <a href="#">Home</a><a href="#">About Us</a><a href="#">Services</a><a href="#">Plans</a><a href="#">Contact Us</a>
    </nav>
  </div>

  <div class="footer-col" style="left:592px">
    <h4>NEWSLETTER</h4>
    <p>Register your email address to get<br>information ablout us</p>
    <div class="email-field">Email Address</div>
    <span class="subscribe">SUBSCRIBE</span>
  </div>

  <div class="footer-col" style="left:906px">
    <h4>CONTACT US</h4>
    <div class="contact-row">
      <svg width="10" height="14" viewBox="0 0 10 14"><path d="M5 0a5 5 0 0 0-5 5c0 3.5 5 9 5 9s5-5.5 5-9a5 5 0 0 0-5-5zm0 7a2 2 0 1 1 0-4 2 2 0 0 1 0 4z" fill="#fff"/></svg>
      <span>Lumabar<br>Harbor Street 22, 10115 Midtown</span>
    </div>
    <div class="contact-row">
      <svg width="12" height="12" viewBox="0 0 12 12"><path d="M2.5 0.5l2 2.5-1.2 1.4a7 7 0 0 0 4.3 4.3l1.4-1.2 2.5 2-1.5 2C5 11.5 0.5 7 0.5 2z" fill="#fff"/></svg>
      <span>+1 555 010 0199</span>
    </div>
    <div class="contact-row">
      <svg width="13" height="10" viewBox="0 0 13 10"><rect x="0" y="0" width="13" height="10" fill="#fff"/><polyline points="0.5,0.5 6.5,5.5 12.5,0.5" fill="none" stroke="#1e1e1e" stroke-width="1.2"/></svg>
      <span>hello@lumabar.example</span>
    </div>
  </div>

  <div class="footer-rule"></div>
  <p class="copyright">Copyrights © 2016, Lumabar. All rights reserved.</p>
  <div class="social" aria-label="Social media links">
    <span></span><span></span><span></span><span></span>
  </div>
</footer>

</body>
</html>
```